I'm looking for an attractive cover to increase sales of my self-published book.
The book is a dystopia science fiction that addresses the subject of autism.
The title is Varno. The name of the author is Denise HOLT. which must appear on the first cover
Expected: 1st cover, 1st cover and 4th cover, for paper and ebook version

The story takes place on earth, not in space. A software manages the daily lives of people, it could be illustrated or not. Two communities are opposed. The book is written in the first person singular, which is the heroine of an 18-year-old woman. The story takes place in Europe, in a rural universe architecture metal glass, with a futuristic metro

The synopsis: Lorene is part of the Elite. She will soon reach her 13th Rainbow, she hopes to be part of the Varno Leaders. She wants to know if anyone can take her place for the next six months. She's going to do everything she can to find out, but she's also going to find out more and question her certainties about Varno. His contacts with the Inferior gradually broke down the barriers separating them. However, it is social contacts that have defined the distinction between Elite and Inferior. In the past, the members of the Elite were a stigmatized minority, the autistic and the Inferior the norm, the neurotypical. And if Lorene's perfect world was not just, should it be preserved or destroyed?

Target Market(s)

The book is aimed at a young adult or adolescent audience

Requirements
Must have
• An ISBN barcode will be placed in a 50.8 mm (2 in.) X 30.5 mm (1.2 in.) White frame in the lower right corner of the back cover.

Cover page size 1 and 4: 12.7 x 20.32cm
Template for the attached cover

Include the price of the book in 4th cover: 9.95 € TTC

Include on the 1st and 4th cover the author's name "Denise Holt" and the title "Varno"

Synopsis in 4th cover in French:

Lorène is part of the Elite. She will soon reach her 13th Rainbow, so she hopes to be part of Varno's Leaders. She wants at all costs to know if someone can take her place during the next 6 months. She will do everything to find out, but she will also discover much more and question her certainties about Varno. His contacts with the Inferior gradually break down the barriers that separate them. Yet it is the social contacts that defined the distinction between Elite and Inferior. In the past, the Elite were a stigmatized minority, the autistic and the Inferior the norm, the neurotypical. And if Lorene's perfect world wasn't fair, should it be preserved or destroyed?

```html
<!DOCTYPE html>
<html lang="fr">
<head>
<meta charset="utf-8">
<title>Varno — couverture</title>
<link rel="stylesheet" href="https://fonts.googleapis.com/css2?family=Michroma&family=Cabin:wght@400;500&display=swap">
<style>
  :root {
    --steel-deep: #0e3f66;
    --steel-mid: #2c86b4;
    --steel-light: #7fd3e6;
    --spine-blue: #1f6494;
    --night: #10283f;
    --title-ice: #bff3f7;
    --title-edge: #5fc6d8;
    --body-text: #f3fbff;
    --skin-warm: #d9894f;
    --glow: #ffd98a;
    --white: #ffffff;
  }
  * { margin: 0; padding: 0; box-sizing: border-box; }
  html, body { width: 1200px; height: 871px; overflow: hidden; background: var(--night); }
  .cover {
    position: relative;
    width: 1200px;
    height: 871px;
    overflow: hidden;
    font-family: "Cabin", sans-serif;
  }

  /* back cover */
  .back {
    position: absolute; left: 0; top: 0; width: 547px; height: 871px;
  }
  .back-art {
    position: absolute; inset: 0;
    background:
      linear-gradient(125deg, transparent 0 40%, rgba(14,63,102,.55) 40% 52%, transparent 52%),
      radial-gradient(ellipse at 30% 25%, var(--steel-light) 0%, var(--steel-mid) 45%, var(--steel-deep) 100%);
  }
  .back-title {
    position: absolute; left: 0; width: 547px; top: 134px;
    text-align: center;
    font-family: "Michroma", sans-serif;
    font-size: 48px; line-height: 1; letter-spacing: 4px;
    font-weight: 400;
    color: var(--title-ice);
    text-shadow: 0 0 6px rgba(95,198,216,.7);
  }
  .back-author {
    position: absolute; left: 0; width: 547px; top: 200px;
    text-align: center;
    font-family: "Michroma", sans-serif;
    font-size: 18px; letter-spacing: 3px;
    color: var(--title-ice);
  }
  .synopsis {
    position: absolute; left: 60px; top: 282px; width: 428px;
    text-align: center;
    font-size: 17.6px; line-height: 21.8px;
    color: var(--body-text);
    text-shadow: 0 1px 2px rgba(8,30,50,.5);
  }
  .price {
    position: absolute; left: 82px; top: 755px;
    font-size: 24px;
    color: var(--body-text);
  }
  .isbn-frame {
    position: absolute; left: 300px; top: 713px; width: 217px; height: 131px;
    background: var(--white);
  }

  /* spine */
  .spine {
    position: absolute; left: 547px; top: 0; width: 106px; height: 871px;
    background: linear-gradient(180deg, var(--spine-blue), #1a5a86 60%, #15466c);
  }
  .spine-art {
    position: absolute; inset: 0;
    background: linear-gradient(160deg, rgba(127,211,230,.25), transparent 60%);
  }
  .spine-title, .spine-author {
    position: absolute; left: 53px;
    font-family: "Michroma", sans-serif;
    color: var(--title-ice);
    white-space: nowrap;
    transform-origin: 0 0;
    transform: rotate(90deg);
  }
  .spine-title { top: 108px; font-size: 46px; letter-spacing: 3px; margin-left: 24px; }
  .spine-author { top: 490px; font-size: 30px; letter-spacing: 3px; margin-left: 16px; }

  /* front cover */
  .front {
    position: absolute; left: 653px; top: 0; width: 547px; height: 871px;
  }
  .front-art {
    position: absolute; inset: 0;
    background:
      radial-gradient(circle at 60% 8%, rgba(255,240,200,.8) 0%, transparent 12%),
      radial-gradient(ellipse at 50% 22%, #4fa6cf 0%, #2a6f9f 35%, transparent 60%),
      linear-gradient(180deg, #2f7eaa 0%, #1c5479 55%, #12324d 100%);
  }
  .portrait-area {
    position: absolute; left: 190px; top: 330px; width: 357px; height: 541px;
    border-radius: 48% 48% 0 0 / 30% 30% 0 0;
    background: radial-gradient(ellipse at 45% 45%, var(--skin-warm) 0%, #a45c38 45%, rgba(40,40,60,.85) 90%);
  }
  .front-title {
    position: absolute; left: 0; width: 547px; top: 100px;
    text-align: center;
    font-family: "Michroma", sans-serif;
    font-size: 86px; line-height: 1; letter-spacing: 5px;
    font-weight: 400;
    color: var(--title-ice);
    padding-left: 20px;
    text-shadow: 0 0 10px rgba(95,198,216,.8), 0 3px 0 var(--title-edge);
  }
  .subtitle {
    position: absolute; left: 0; width: 547px; top: 208px;
    text-align: center;
    font-family: "Michroma", sans-serif;
    font-size: 21px; letter-spacing: 3px;
    color: var(--title-ice);
    padding-left: 28px;
  }
  .front-author {
    position: absolute; left: 0; width: 547px; top: 776px;
    text-align: center;
    font-family: "Michroma", sans-serif;
    font-size: 32px; letter-spacing: 3px;
    color: var(--title-ice);
    padding-left: 60px;
  }
  .front-glow {
    position: absolute; left: 0; top: 840px; width: 547px; height: 3px;
    background: linear-gradient(90deg, transparent, var(--glow), transparent);
    opacity: .6;
  }
</style>
</head>
<body>
<div class="cover">

  <section class="back">
    <div class="back-art" role="img" aria-label="Photographie d'une structure futuriste en acier et verre, teintée de bleu"></div>
    <h2 class="back-title">VARNO</h2>
    <p class="back-author">DENISE HOLT</p>
    <p class="synopsis">Lorène fait partie de l’Elite. Elle va bientôt atteindre son 13ème Arc-en-Ciel, elle espère pouvoir alors faire partie des Leaders de Varno. Elle veut à tout prix savoir si quelqu’un peut prendre sa place durant les 6 mois à venir. Elle va tout faire pour le découvrir, mais elle va aussi découvrir bien plus et remettre en question ses certitudes sur Varno. Ses contacts avec les Inferior brisent peu à peu les barrières qui les séparent. Ce sont pourtant les contacts sociaux qui ont défini la distinction entre Elite et Inferior. Autrefois, les membres de l’Elite étaient une minorité stigmatisée, les autistes et les Inferior la norme, les neurotypiques. Et si le monde si parfait de Lorène n’était pas juste, faudrait-il le conserver ou le détruire ?</p>
    <p class="price">9,95 € TTC</p>
    <div class="isbn-frame"></div>
  </section>

  <section class="spine">
    <div class="spine-art"></div>
    <span class="spine-title">VARNO</span>
    <span class="spine-author">DENISE HOLT</span>
  </section>

  <section class="front">
    <div class="front-art" role="img" aria-label="Illustration d'une sphère en pièces de puzzle lumineuse au-dessus d'une station de métro futuriste"></div>
    <div class="portrait-area" role="img" aria-label="Portrait illustré de l'héroïne, une jeune femme aux cheveux longs"></div>
    <h1 class="front-title">VARNO</h1>
    <p class="subtitle">L'UNIVERS DE L'AUTISME</p>
    <p class="front-author">DENISE HOLT</p>
    <div class="front-glow"></div>
  </section>

</div>
</body>
</html>
```